Power Point CI

Creat a Slide Master which we can use and also add new slides with bullets, or other graphic design which we can fill. Power Point Master Format - also amend the graphics on the PPT - especially the project roadmap or profile page. have a look on our website www.talvoreksa.io. I would also appreciate other slides which we can use and fill

Target Market(s)

companies - PE, HR Executive

Industry/Entity Type

Executive Search

Font styles to use
Serif
Other font styles liked:
• Calibri or Coast like on our website

Colors
0094D4
00A9DD
6FCCEA
C7EBF8
E9F6FB

Requirements
Must have
• needs to sleek and slim - prefer white and bright elegant Backgrounds
Nice to have
• it should somehow fit to our website and corporate CI
Should not have
• Full green CI

```html
<!DOCTYPE html>
<html lang="en">
<head>
<meta charset="utf-8">
<title>Talvoreksa – Presentation Master</title>
<link href="https://fonts.googleapis.com/css2?family=Open+Sans:wght@300;400;600;700&display=swap" rel="stylesheet">
<style>
:root{
  --stage:#dcdadb;
  --teal:#0d5c75;
  --teal-deep:#064a60;
  --teal-soft:#1b6d86;
  --ink:#0d5c75;
  --grey:#6d6d6d;
  --row:#f1f1f1;
  --light:#c9e4ef;
  --white:#ffffff;
}
*{margin:0;padding:0;box-sizing:border-box}
html,body{width:1200px;height:2484px;overflow:hidden;background:var(--stage);font-family:"Open Sans",sans-serif}
.canvas{position:relative;width:1200px;height:2484px}
.hero{position:absolute;left:160px;top:85px;width:880px;height:495px;overflow:hidden}
.hero .slide{position:absolute;left:0;top:0;transform:scale(1.6296);transform-origin:0 0}
.grid .slide{position:absolute}
.slide{width:540px;height:304px;background:var(--white);overflow:hidden;position:relative}
.slide.dark .field{position:absolute;left:0;top:0;width:540px;height:272px;background:var(--teal)}
.facets{position:absolute;left:0;top:0}
.cities{position:absolute;left:0;bottom:0;width:100%;height:32px;line-height:32px;text-align:center;font-size:8.2px;letter-spacing:1.4px;color:var(--teal)}
.emblem-area{position:absolute;border-radius:18px;background:linear-gradient(135deg,rgba(214,235,244,.55),rgba(150,204,226,.25))}
.wordmark{position:absolute;color:var(--white);font-weight:300;letter-spacing:3px;display:flex;align-items:center;gap:8px}
.wordmark .dot{width:10px;height:10px;border-radius:50%;background:var(--light)}
.cover-title{position:absolute;color:var(--white);font-weight:700;font-size:25px;line-height:29px}
.lede{position:absolute;color:var(--white);font-size:6.6px;line-height:8px}
.date{position:absolute;color:var(--white);font-size:5.6px}
.date-pill{position:absolute;border:1px solid var(--white);border-radius:3px;color:var(--white);font-size:5.6px;font-weight:700;padding:6px 16px}
.heading{position:absolute;left:31px;top:26px;color:var(--ink);font-weight:700;font-size:19.5px;line-height:21px}
.body{position:absolute;color:var(--grey);font-size:6.6px;line-height:7.4px}
.body p{margin-bottom:5px}
.portrait{position:absolute;left:304px;top:0;width:210px;height:252px;background:linear-gradient(160deg,#5b5b5b,#2b2b2b 60%,#1b1b1b)}
.footer{position:absolute;left:0;top:262px;width:540px;height:36px}
.footer .mark{position:absolute;left:16px;top:2px;width:14px;height:14px;border-radius:50%;background:var(--light)}
.footer .band{position:absolute;left:11px;top:18px;width:518px;height:17px;border-radius:9px;background:var(--teal);color:var(--white);font-size:4.8px;line-height:17px;text-align:right;padding-right:22px}
.footer .band .page{display:inline-block;border-left:1px solid rgba(255,255,255,.6);margin-left:10px;padding-left:10px;font-weight:700}
.bullets{position:absolute;list-style:none;color:var(--grey);font-size:6.6px;line-height:7.4px}
.bullets li{position:relative;padding-left:12px;margin-bottom:6px}
.bullets li::before{content:"";position:absolute;left:1px;top:2.5px;width:2.5px;height:2.5px;background:var(--teal)}
.bullets b{color:var(--teal);font-weight:700}
.values{position:absolute;left:0;top:78px;width:540px}
.values .rule{position:absolute;left:0;top:14px;width:540px;border-top:1px dashed #8fb6c5}
.value{position:absolute;top:0;width:108px;text-align:center}
.value .icon{width:30px;height:30px;margin:0 auto;border-radius:50%;background:var(--teal);position:relative}
.value h4{color:var(--teal);font-size:7.6px;font-weight:700;margin-top:9px}
.value p{color:var(--grey);font-size:5.6px;line-height:6.5px;margin-top:9px}
.refs{position:absolute;top:90px;width:232px}
.refs h4{color:var(--teal);font-size:8.6px;font-weight:700;margin-bottom:10px;padding-left:4px}
.refs table{width:100%;border-collapse:collapse;font-size:5.6px}
.refs td{height:23px;padding-left:4px}
.refs tr:nth-child(odd) td{background:var(--row)}
.refs td:first-child{color:var(--teal);font-weight:700;width:116px}
.refs td:last-child{color:#333}
.phases{position:absolute;left:0;top:62px;width:540px}
.phase-label{position:absolute;top:0;font-size:6.4px;font-weight:700;color:var(--teal)}
.phase-band{position:absolute;left:0;top:11px;width:540px;height:20px;background:var(--teal-deep)}
.phase-band span{position:absolute;top:0;line-height:20px;color:var(--white);font-size:5.8px}
.step{position:absolute;width:96px;text-align:center}
.step .icon{width:34px;height:34px;border-radius:50%;background:var(--teal);margin:0 auto}
.step h5{color:var(--teal);font-size:6.8px;font-weight:700;margin-top:6px;line-height:7px}
.step p{color:var(--grey);font-size:5.2px;line-height:6px;margin-top:4px}
.contact{position:absolute;left:283px;top:160px;color:var(--white)}
.contact h4{font-size:10px;font-weight:600;margin-bottom:12px}
.contact li{list-style:none;font-size:6.8px;display:flex;align-items:center;gap:8px;margin-bottom:8px}
</style>
</head>
<body>
<div class="canvas">

<!-- Hero: cover slide enlarged -->
<section class="hero">
  <div class="slide dark">
    <div class="field"></div>
    <svg class="facets" width="540" height="272" viewBox="0 0 540 272">
      <polygon points="260,0 540,0 540,120" fill="#064a60" opacity=".55"/>
      <polygon points="300,272 540,60 540,272" fill="#ffffff" opacity=".06"/>
      <polygon points="0,160 120,272 0,272" fill="#064a60" opacity=".4"/>
      <polygon points="420,0 540,0 540,40" fill="#ffffff" opacity=".05"/>
    </svg>
    <div class="emblem-area" role="img" aria-label="Large brand emblem artwork" style="left:20px;top:8px;width:270px;height:258px"></div>
    <h1 class="cover-title" style="left:267px;top:104px">Presentation<br>Title Goes Here!</h1>
    <p class="lede" style="left:267px;top:180px;width:215px">Lorem ipsum dolor sit amet, consectetur adipiscing elit. Vivamus eu dui ex. Curabitur dapibus dignissim dui, in molestie metus feugiat sed.</p>
    <p class="date" style="left:267px;top:224px">Friday, April 21, 2023</p>
    <p class="cities">Hamburg | Wien | Berlin | &nbsp;München</p>
  </div>
</section>

<div class="grid">

<!-- 1 Cover -->
<div class="slide dark" style="left:51px;top:835px">
  <div class="field"></div>
  <svg class="facets" width="540" height="272" viewBox="0 0 540 272">
    <polygon points="260,0 540,0 540,120" fill="#064a60" opacity=".55"/>
    <polygon points="300,272 540,60 540,272" fill="#ffffff" opacity=".06"/>
    <polygon points="0,160 120,272 0,272" fill="#064a60" opacity=".4"/>
  </svg>
  <div class="emblem-area" role="img" aria-label="Large brand emblem artwork" style="left:14px;top:6px;width:262px;height:262px"></div>
  <h1 class="cover-title" style="left:268px;top:103px">Presentation<br>Title Goes Here!</h1>
  <p class="lede" style="left:268px;top:180px;width:215px">Lorem ipsum dolor sit amet, consectetur adipiscing elit. Vivamus eu dui ex. Curabitur dapibus dignissim dui, in molestie metus feugiat sed.</p>
  <p class="date" style="left:268px;top:222px">Friday, April 21, 2023</p>
  <p class="cities">Hamburg | Wien | Berlin | &nbsp;München</p>
</div>

<!-- 2 Brand divider -->
<div class="slide dark" style="left:609px;top:835px">
  <div class="field"></div>
  <svg class="facets" width="540" height="272" viewBox="0 0 540 272">
    <polygon points="0,0 200,0 0,140" fill="#064a60" opacity=".45"/>
    <polygon points="280,272 540,40 540,272" fill="#ffffff" opacity=".06"/>
    <polygon points="360,0 540,0 540,90" fill="#064a60" opacity=".5"/>
  </svg>
  <div class="wordmark" style="left:150px;top:156px;font-size:23px"><span class="dot" style="width:16px;height:16px"></span>TALVOREKSA</div>
  <p class="cities">Hamburg | Wien | Berlin | &nbsp;München</p>
</div>

<!-- 3 Title variant -->
<div class="slide dark" style="left:51px;top:1157px">
  <div class="field"></div>
  <svg class="facets" width="540" height="272" viewBox="0 0 540 272">
    <polygon points="260,0 540,0 540,120" fill="#064a60" opacity=".55"/>
    <polygon points="300,272 540,60 540,272" fill="#ffffff" opacity=".06"/>
  </svg>
  <div class="wordmark" style="left:38px;top:66px;font-size:12px"><span class="dot"></span>TALVOREKSA</div>
  <h1 class="cover-title" style="left:43px;top:112px">Presentation Title<br>Goes Here!</h1>
  <p class="lede" style="left:43px;top:178px;width:280px">Lorem ipsum dolor sit amet, consectetur adipiscing elit. Vivamus eu dui ex. Curabitur dapibus dignissim dui, in molestie metus feugiat sed. Praesent aliquet lorem ex, eu dapibus odio varius at.</p>
  <p class="date-pill" style="left:43px;top:214px">Friday, April 21, 2023</p>
  <p class="cities">Hamburg | Wien | Berlin | &nbsp;München</p>
</div>

<!-- 4 Profile -->
<div class="slide" style="left:609px;top:1157px">
  <h2 class="heading" style="top:28px">Dr. Marit<br>Ellhoven</h2>
  <div class="body" style="left:31px;top:98px;width:255px">
    <p>Marit knows what modern management is all about, and that from many points of view – she has not only successfully appointed many to leadership positions, but she has held those positions herself several times.</p>
    <p>As a graduate of medicine of the Lindenau Clinic, she first started working for Brightwell Partners, where she led the Brightwell Hospital Academy. At Kessling &amp; Roe, she was responsible for the German healthcare sector. She was a founder and CEO of a healthcare tech start-up, which she successfully sold to an investor. And she was the CHRO of another startup that scaled very fast. To share this experience with many companies, she founded Talvoreksa Executive Search in 2021.</p>
    <p>Marit lives in Hamburg with her family.</p>
  </div>
  <div class="portrait" role="img" aria-label="Portrait photo of Dr. Marit Ellhoven"></div>
  <div class="footer"><span class="mark"></span><div class="band">https://talvoreksa.io<span class="page">4</span></div></div>
</div>

<!-- 5 Profile -->
<div class="slide" style="left:51px;top:1479px">
  <h2 class="heading" style="top:30px">Selma Drovik</h2>
  <div class="body" style="left:31px;top:98px;width:255px">
    <p>Selma started her career as a Global Product Manager at Norvant Tools in Schaan before she spent 3 years in London as the European Sales Manager for Aerolis Air.</p>
    <p>She then accepted an offer from Kessling &amp; Roe where she learned the skills of research.</p>
    <p>When her partner was transferred to Bogota in Colombia, she became self-employed (working primarily for Kessling &amp; Roe), and now, back in Vienna, she founded Talvoreksa Executive Search together with Marit.</p>
    <p>Selma studied International Business Administration at the Danube School of Business and also graduated from the GEMBA programme. She is mother of 2 children.</p>
  </div>
  <div class="portrait" role="img" aria-label="Portrait photo of Selma Drovik"></div>
  <div class="footer"><span class="mark"></span><div class="band">https://talvoreksa.io<span class="page">5</span></div></div>
</div>

<!-- 6 Bullets -->
<div class="slide" style="left:609px;top:1479px">
  <h2 class="heading" style="top:30px">Who We Are and How We Work</h2>
  <ul class="bullets" style="left:31px;top:100px;width:215px">
    <li><b>Longstanding experience</b> with a passion for placing (C-Level) Executives in Healthcare and other industries</li>
    <li>In-depth expertise strong networks in healthcare, covering all <b>relevant sub-sectors</b> (HC Services, PE Healthcare Rollups, Elderly Care Chains, Physiotherapy, Digital Health, Medical Technology, Healthcare IT), including relevant expertise regarding the regulatory environment in Germany</li>
    <li>Expertise beyond placement and HR topics, allowing for eye-level discussion around your business</li>
    <li><b>Creative approaches</b> to finding – and convincing – candidates</li>
  </ul>
  <ul class="bullets" style="left:287px;top:100px;width:220px">
    <li><b>Structured</b> and lean <b>digital search processes</b>, high transparency, comprehensive candidate evaluation</li>
    <li><b>Referencing</b> of candidates as part of the search process; psychometrics on demand</li>
    <li>Onboarding support to ensure a good start for the candidate</li>
    <li>We work with you <b>personally</b> and act as an <b>ambassador</b> for our clients in the market</li>
  </ul>
  <div class="footer"><span class="mark"></span><div class="band">https://talvoreksa.io<span class="page">6</span></div></div>
</div>

<!-- 7 Values -->
<div class="slide" style="left:51px;top:1801px">
  <h2 class="heading" style="top:30px">Our Values</h2>
  <div class="values">
    <div class="rule"></div>
    <div class="value" style="left:31px"><div class="icon"><svg width="30" height="30" viewBox="0 0 30 30"><path d="M15 21 C8 16 9 10 12.5 10 C14 10 15 11.5 15 11.5 C15 11.5 16 10 17.5 10 C21 10 22 16 15 21Z" fill="#fff"/></svg></div><h4>HONEST</h4><p>We only work with clients who can benefit from our expertise. We are not interested in status symbols, only in achieving results in a way that is transparent and beneficial for everyone.</p></div>
    <div class="value" style="left:155px"><div class="icon"><svg width="30" height="30" viewBox="0 0 30 30"><circle cx="15" cy="11.5" r="4" fill="#fff"/><path d="M8 22 C8 17 22 17 22 22Z" fill="#fff"/></svg></div><h4>PERSONAL</h4><p>We put all of our resources into finding you the top talents you are looking for – and we get involved ourselves. We have excellent networks, and we are always hot on the heels of fresh talent. That is how we find the people that you need right now. And we help them realise that your company is the right place for them.</p></div>
    <div class="value" style="left:279px"><div class="icon"><svg width="30" height="30" viewBox="0 0 30 30"><circle cx="15" cy="15" r="6" fill="none" stroke="#fff" stroke-width="2.4" stroke-dasharray="3 1.6"/><circle cx="15" cy="15" r="2" fill="#fff"/></svg></div><h4>PRAGMATIC</h4><p>We work fast. But we don't start until we have a clear goal: We begin by asking "How will you know the appointment was successful, 3 years from now?" This thought drives our process – streamlined, digital, and constantly in communication with you, from the briefing to your new staff member's first day.</p></div>
    <div class="value" style="left:402px"><div class="icon"><svg width="30" height="30" viewBox="0 0 30 30"><circle cx="11" cy="12" r="2.6" fill="#fff"/><circle cx="19" cy="12" r="2.6" fill="#fff"/><circle cx="15" cy="17" r="2.6" fill="#fff"/><path d="M10 23 C10 19.5 20 19.5 20 23Z" fill="#fff"/></svg></div><h4>DIVERSE</h4><p>We know where the obstacles lie, and we know where things get tough – we have worked through them ourselves, as employees, as managers, as founders, and as mothers. That's how we know how diversity really works, and how diversity can best benefit your company.</p></div>
  </div>
  <div class="footer"><span class="mark"></span><div class="band">https://talvoreksa.io<span class="page">7</span></div></div>
</div>

<!-- 8 References table -->
<div class="slide" style="left:609px;top:1801px">
  <h2 class="heading" style="top:30px">Relevant reference assignments (excerpt)</h2>
  <div class="refs" style="left:27px">
    <h4>POSITION TO BE DEFINED</h4>
    <table>
      <tr><td>Explanation</td><td>Investor/Owner</td></tr>
      <tr><td>Explanation</td><td>Investor/Owner</td></tr>
      <tr><td>Explanation</td><td>Investor/Owner</td></tr>
      <tr><td>Explanation</td><td>Investor/Owner</td></tr>
      <tr><td>Explanation</td><td>Investor/Owner</td></tr>
    </table>
  </div>
  <div class="refs" style="left:282px">
    <h4>POSITION TO BE DEFINED</h4>
    <table>
      <tr><td>Explanation</td><td>Investor/Owner</td></tr>
      <tr><td>Explanation</td><td>Investor/Owner</td></tr>
      <tr><td>Explanation</td><td>Investor/Owner</td></tr>
      <tr><td>Explanation</td><td>Investor/Owner</td></tr>
      <tr><td>Explanation</td><td>Investor/Owner</td></tr>
    </table>
  </div>
  <div class="footer"><span class="mark"></span><div class="band">https://talvoreksa.io<span class="page">8</span></div></div>
</div>

<!-- 9 Search process roadmap -->
<div class="slide" style="left:51px;top:2122px">
  <h2 class="heading" style="top:30px">Search Process</h2>
  <div class="phases">
    <span class="phase-label" style="left:98px">Phase 1</span>
    <span class="phase-label" style="left:264px">Phase 2</span>
    <span class="phase-label" style="left:430px">Phase 3</span>
    <div class="phase-band">
      <span style="left:83px">Research - Longlist</span>
      <span style="left:233px">Focus &amp; Interviews - Shortlist</span>
      <span style="left:425px">Completion</span>
      <svg style="position:absolute;left:188px;top:0" width="12" height="20"><path d="M2 2 L10 10 L2 18" fill="none" stroke="#1b6d86" stroke-width="3"/></svg>
      <svg style="position:absolute;left:358px;top:0" width="12" height="20"><path d="M2 2 L10 10 L2 18" fill="none" stroke="#1b6d86" stroke-width="3"/></svg>
    </div>
  </div>
  <svg style="position:absolute;left:0;top:100px" width="540" height="70">
    <line x1="0" y1="10" x2="540" y2="10" stroke="#0d5c75" stroke-dasharray="2 2" stroke-width=".8"/>
    <g fill="#0d5c75">
      <circle cx="60" cy="10" r="3.5"/><circle cx="165" cy="10" r="3.5"/><circle cx="270" cy="10" r="3.5"/><circle cx="375" cy="10" r="3.5"/><circle cx="480" cy="10" r="3.5"/>
    </g>
    <g stroke="#0d5c75" stroke-width=".8">
      <line x1="60" y1="10" x2="60" y2="32"/><line x1="165" y1="10" x2="165" y2="66"/><line x1="270" y1="10" x2="270" y2="32"/><line x1="375" y1="10" x2="375" y2="66"/><line x1="480" y1="10" x2="480" y2="32"/>
    </g>
    <text x="20" y="22" font-size="5.4" fill="#0d5c75" font-family="Open Sans, sans-serif">CW 1</text>
    <text x="505" y="22" font-size="5.4" fill="#0d5c75" font-family="Open Sans, sans-serif">CW 2</text>
  </svg>
  <div class="step" style="left:12px;top:132px"><div class="icon"></div><h5>Kickoff</h5><p>Discuss and agree on profile, position specification and target list.</p></div>
  <div class="step" style="left:117px;top:166px"><div class="icon"><svg width="34" height="34"><circle cx="15" cy="15" r="5.5" fill="none" stroke="#fff" stroke-width="2.2"/><line x1="19" y1="19" x2="24" y2="24" stroke="#fff" stroke-width="2.4"/></svg></div><h5>Research</h5><p>Active and passive research, approach of potential candidates</p></div>
  <div class="step" style="left:222px;top:132px"><div class="icon"></div><h5>Interviews</h5><p>Presentation of prioritised profiles, client interviews</p></div>
  <div class="step" style="left:327px;top:166px"><div class="icon"></div><h5>References</h5><p>Assessments (optional), taking references</p></div>
  <div class="step" style="left:432px;top:132px"><div class="icon"></div><h5>Selection final<br>candidate</h5><p>Contract negotiation and onboarding, feedback discussion</p></div>
  <div class="footer"><span class="mark"></span><div class="band">https://talvoreksa.io<span class="page">9</span></div></div>
</div>

<!-- 10 Thank you -->
<div class="slide dark" style="left:609px;top:2122px">
  <div class="field"></div>
  <svg class="facets" width="540" height="272" viewBox="0 0 540 272">
    <polygon points="260,0 540,0 540,120" fill="#064a60" opacity=".55"/>
    <polygon points="300,272 540,60 540,272" fill="#ffffff" opacity=".06"/>
  </svg>
  <div class="emblem-area" role="img" aria-label="Large brand emblem artwork" style="left:14px;top:6px;width:262px;height:262px"></div>
  <h1 class="cover-title" style="left:283px;top:100px">Thank you!</h1>
  <div class="contact">
    <h4>Contact Us</h4>
    <ul>
      <li><svg width="9" height="9" viewBox="0 0 10 10"><path d="M2 1 L4 1 L5 3.5 L3.8 4.5 C4.5 6 5 6.5 6.5 7.2 L7.5 6 L10 7 L10 9 C5 9.5 0.5 5 1 1Z" fill="#fff"/></svg>Phone Number Goes Here</li>
      <li><svg width="9" height="9" viewBox="0 0 10 10"><circle cx="5" cy="5" r="4" fill="none" stroke="#fff" stroke-width="1.2"/><circle cx="5" cy="5" r="1.6" fill="none" stroke="#fff" stroke-width="1.1"/></svg>E-Mail Address Goes Here</li>
      <li><svg width="9" height="9" viewBox="0 0 10 10"><circle cx="5" cy="5" r="4" fill="none" stroke="#fff" stroke-width="1"/><ellipse cx="5" cy="5" rx="1.8" ry="4" fill="none" stroke="#fff" stroke-width=".8"/><line x1="1" y1="5" x2="9" y2="5" stroke="#fff" stroke-width=".8"/></svg>URL Address Goes Here</li>
    </ul>
  </div>
  <p class="cities">Hamburg | Wien | Berlin | &nbsp;München</p>
</div>

</div>
</div>
</body>
</html>
```